Bref créative
KTR stationery
Simple
Samir Haddoud
Managing Director
Dubai Office:
P.O. Box 48213, Dubai, UAE
T: +971 4 5708812
Beirut Office:
Solvira Hotel & Resort - Corniche
Rue des Tilleuls Avenue
Zaitouné 4157 2203, Beirut, Lebanon
T: +961 1 537204
samir@koratecholding.example
www.koratecholding.example
directly under name and title, pls put
M: +971 55 8064139

```html
<!DOCTYPE html>
<html lang="en">
<head>
<meta charset="utf-8">
<title>KTR Stationery</title>
<link href="https://fonts.googleapis.com/css2?family=Open+Sans:wght@400;600;700&display=swap" rel="stylesheet">
<style>
:root{
  --board-top:#a8693c;
  --board-bottom:#6f3f22;
  --paper:#ffffff;
  --brand-red:#c1272d;
  --brand-red-dark:#8e1a1f;
  --brand-blue:#1d8fd6;
  --brand-blue-dark:#0f5f9e;
  --text-grey:#6b6b6b;
  --stripe-navy:#223a7a;
}
*{box-sizing:border-box;margin:0;padding:0}
html,body{width:1200px;height:607px;overflow:hidden}
body{
  position:relative;
  font-family:"Open Sans",Arial,sans-serif;
  background:linear-gradient(160deg,var(--board-top),var(--board-bottom));
}
.piece{position:absolute;background:var(--paper);box-shadow:0 2px 6px rgba(0,0,0,.35);overflow:hidden}
.wordmark{font-weight:700;color:var(--brand-red);letter-spacing:1px;line-height:1}

/* Business card front */
.card{width:187px;height:125px;left:24px}
.card--front-a{top:19px}
.card--front-b{top:319px}
.card .holder{position:absolute;left:9px;top:8px}
.card .holder-name{font-size:9px;font-weight:700;color:var(--brand-red)}
.card .holder-title{font-size:5px;color:var(--text-grey)}
.card .holder-mobile{font-size:5px;color:var(--text-grey)}
.card .wordmark{position:absolute;left:12px;top:48px;font-size:22px}
.card .contacts{position:absolute;left:96px;top:8px;width:86px;font-size:4px;line-height:1.4;color:var(--text-grey)}
.card .contacts b{color:var(--brand-red);font-weight:700}
.card .band{position:absolute;left:0;right:0;bottom:10px;height:12px;background:var(--brand-blue)}
.card .band-light{position:absolute;left:0;right:0;bottom:5px;height:5px;background:#cfe6f5}
.stripes{position:absolute;right:8px;bottom:5px;width:28px;height:22px;
  background:repeating-linear-gradient(90deg,var(--brand-red) 0 4px,#fff 4px 6px)}
.card .web{position:absolute;left:9px;bottom:0;font-size:4px;color:var(--text-grey)}

/* Card backs */
.card--back-blue{top:173px;background:linear-gradient(135deg,var(--brand-blue),var(--brand-blue-dark))}
.card--back-red{top:468px;background:linear-gradient(135deg,var(--brand-red),var(--brand-red-dark))}
.card-back .wordmark{position:absolute;left:0;right:0;top:50px;text-align:center;font-size:22px;color:#fff}
.card-back .web{position:absolute;left:9px;bottom:6px;font-size:4px;color:#fff}

/* Letterhead */
.letterhead{left:233px;top:24px;width:410px;height:564px}
.letterhead .wordmark{position:absolute;left:0;right:0;top:40px;text-align:center;font-size:48px}
.letterhead .footer{position:absolute;left:10px;bottom:22px;font-size:5px;line-height:1.5;color:var(--text-grey)}
.letterhead .footer b{color:var(--brand-red)}
.letterhead .band{position:absolute;left:0;right:40px;bottom:8px;height:12px;background:var(--brand-blue)}
.letterhead .email{position:absolute;left:10px;bottom:10px;font-size:5px;color:#fff}
.letterhead .stripes{right:6px;bottom:6px;width:32px;height:20px}

/* Compliment slip */
.slip{left:694px;top:48px;width:487px;height:264px}
.slip .wordmark{position:absolute;left:22px;top:70px;font-size:44px}
.slip .footer{position:absolute;left:22px;top:202px;font-size:5px;line-height:1.6;color:var(--text-grey)}
.slip .footer b{color:var(--brand-red)}
.slip .band{position:absolute;left:0;right:40px;top:228px;height:14px;background:var(--brand-blue)}
.slip .email{position:absolute;left:22px;top:232px;font-size:5px;color:#fff}
.slip .stripes{right:6px;top:224px;bottom:auto;width:32px;height:22px}

/* Envelope */
.envelope{left:694px;top:336px;width:487px;height:240px;background:transparent;box-shadow:none}
.envelope .body{position:absolute;left:0;right:0;top:0;bottom:0;background:var(--paper);box-shadow:0 2px 6px rgba(0,0,0,.35)}
.envelope svg{position:absolute;left:0;top:0}
.envelope .wordmark{position:absolute;left:0;right:0;top:32px;text-align:center;font-size:24px;color:#fff}
.envelope .web{position:absolute;left:14px;top:126px;font-size:5px;color:var(--text-grey)}
</style>
</head>
<body>

<div class="piece card card--front-a">
  <div class="holder">
    <div class="holder-name">Samir Haddoud</div>
    <div class="holder-title">Managing Director</div>
    <div class="holder-mobile">M: +971 55 8064139</div>
  </div>
  <div class="wordmark">KTR</div>
  <div class="contacts">
    <b>Dubai Office</b><br>P.O. Box 48213, Dubai, UAE<br>T: +971 4 5708812<br>
    <b>Beirut Office</b><br>Solvira Hotel &amp; Resort - Corniche<br>Rue des Tilleuls Avenue<br>Zaitouné 4157 2203, Beirut, Lebanon<br>T: +961 1 537204<br>samir@koratecholding.example
  </div>
  <div class="band"></div><div class="band-light"></div>
  <div class="stripes"></div>
</div>

<div class="piece card card-back card--back-blue">
  <div class="wordmark">KTR</div>
  <div class="web">www.koratecholding.example</div>
</div>

<div class="piece card card--front-b">
  <div class="holder">
    <div class="holder-name">Samir Haddoud</div>
    <div class="holder-title">Managing Director</div>
    <div class="holder-mobile">M: +971 55 8064139</div>
  </div>
  <div class="wordmark">KTR</div>
  <div class="contacts">
    <b>Dubai Office</b><br>P.O. Box 48213, Dubai, UAE<br>T: +971 4 5708812<br>
    <b>Beirut Office</b><br>Solvira Hotel &amp; Resort - Corniche<br>Rue des Tilleuls Avenue<br>Zaitouné 4157 2203, Beirut, Lebanon<br>T: +961 1 537204<br>samir@koratecholding.example
  </div>
  <div class="band"></div><div class="band-light"></div>
  <div class="stripes"></div>
</div>

<div class="piece card card-back card--back-red">
  <div class="wordmark">KTR</div>
  <div class="web">www.koratecholding.example</div>
</div>

<div class="piece letterhead">
  <div class="wordmark">KTR</div>
  <div class="footer">
    <b>Dubai Office</b> P.O. Box 48213, Dubai, UAE | T: +971 4 5708812<br>
    <b>Beirut Office</b> Solvira Hotel &amp; Resort - Corniche, Rue des Tilleuls Avenue, Zaitouné 4157 2203, Beirut, Lebanon | T: +961 1 537204
  </div>
  <div class="band"></div>
  <div class="email">samir@koratecholding.example</div>
  <div class="stripes"></div>
</div>

<div class="piece slip">
  <div class="wordmark">KTR</div>
  <div class="footer">
    <b>Dubai Office</b> P.O. Box 48213, Dubai, UAE | T: +971 4 5708812<br>
    <b>Beirut Office</b> Solvira Hotel &amp; Resort - Corniche, Rue des Tilleuls Avenue, Zaitouné 4157 2203, Beirut, Lebanon | T: +961 1 537204
  </div>
  <div class="band"></div>
  <div class="email">www.koratecholding.example</div>
  <div class="stripes"></div>
</div>

<div class="piece envelope">
  <div class="body"></div>
  <svg width="487" height="110" viewBox="0 0 487 110" aria-hidden="true">
    <defs>
      <linearGradient id="flapFill" x1="0" y1="0" x2="0" y2="1">
        <stop offset="0" stop-color="#1d8fd6"/>
        <stop offset="1" stop-color="#0f5f9e"/>
      </linearGradient>
    </defs>
    <path d="M0 0 H487 V60 Q487 70 470 74 L260 104 Q243 107 226 104 L17 74 Q0 70 0 60 Z" fill="url(#flapFill)"/>
  </svg>
  <div class="wordmark">KTR</div>
  <div class="web">www.koratecholding.example</div>
</div>

</body>
</html>
```